rk harbour excursions website for fish guide business in Campbell river Bc

looking for website to promote my fishing guide buisiness and its charters

Have uploaded a pictures of my boat not sure which one…
Also two pictures of a fish caught and one of a fish cleaning station

Have added script for website

Target Market(s)

Visitors to Campbell River BC who want fish and or go whale / wildlife adventure tour

Industry/Entity Type

Tourism

Coding

Coded - Design and coding required

Number of Pages Required

5+ page

Font styles to use
Sans Serif

Requirements
Must have
• New email is info@rkharbourexcursions…. Delete the word halibut…. Add second contact Lou 2507394216….Pictures and my logo … place for videos
Should not have
• should not have a boat picture which is not supplied

```html
<!DOCTYPE html>
<html lang="en">
<head>
<meta charset="utf-8">
<title>RK Harbour Excursions – Campbell River Fishing Charters</title>
<link rel="stylesheet" href="https://fonts.googleapis.com/css2?family=Poppins:wght@400;500;600;700&display=swap">
<style>
:root{
  --navy:#2a2265;
  --navy-deep:#221b57;
  --orange:#f76b0a;
  --lavender:#eeebfb;
  --ink:#3a3a3a;
  --footer:#2b2b2b;
  --white:#ffffff;
}
*{box-sizing:border-box;margin:0;padding:0}
html,body{width:1200px;height:4747px;overflow:hidden}
body{font-family:"Poppins",sans-serif;color:var(--ink);background:var(--white);position:relative}
.abs{position:absolute}
h1,h2{font-family:"Poppins",sans-serif;font-weight:700;color:var(--navy);letter-spacing:.3px}
p{font-size:16.5px;line-height:34px}
a{color:inherit}
.btn{display:flex;align-items:center;justify-content:center;background:var(--orange);color:#fff;font-weight:600;font-size:21px;border-radius:34px;text-decoration:none;width:360px;height:64px}

/* header */
.site-header{left:0;top:0;width:1200px;height:115px;background:#fff}
.header-email{left:74px;top:38px;display:flex;align-items:center;gap:14px;font-size:15px;color:var(--navy);font-weight:500}
.mail-dot{width:38px;height:38px;border-radius:50%;background:#333;display:flex;align-items:center;justify-content:center}
.brand{left:512px;top:20px;width:176px;height:176px;border-radius:50%;background:#fff;border:5px solid var(--navy);display:flex;align-items:center;justify-content:center;text-align:center;font-weight:700;color:var(--navy);font-size:21px;line-height:26px;z-index:3}
.nav{right:74px;top:44px;display:flex;gap:36px;font-size:18px;font-weight:500;color:#555}
.nav .current{color:var(--navy);font-weight:600}

/* hero */
.hero{left:0;top:115px;width:1200px;height:623px;background:linear-gradient(180deg,#8a98a6 0%,#5b6f86 28%,#2f4a78 50%,#223e70 75%,#1b2f5a 100%)}
.hero h1{position:absolute;left:0;width:1200px;top:255px;text-align:center;color:#fff;font-size:50px;line-height:54px}
.hero .btn{position:absolute;left:420px;top:402px}

.photo{display:block}
.panel-lav{background:var(--lavender)}
.dark{background:var(--navy)}
.dark h2,.dark p{color:#fff}
.feature h2{font-size:40px;line-height:52px}

.play{position:absolute;left:50%;top:50%;transform:translate(-50%,-50%)}

/* footer */
.site-footer{left:0;top:4400px;width:1200px;height:270px;background:var(--footer);color:#fff}
.foot-brand{left:76px;top:68px;width:146px;height:146px;border-radius:50%;background:#fff;border:4px solid var(--navy);color:var(--navy);font-weight:700;font-size:15px;line-height:19px;display:flex;align-items:center;justify-content:center;text-align:center}
.foot-col h3{font-size:21px;font-weight:600;margin-bottom:14px}
.foot-col p{font-size:13.5px;line-height:28px;color:#ddd}
.addr-row{display:flex;gap:14px;font-size:13.5px;line-height:24px;color:#ddd;margin-bottom:12px}
.social{display:flex;gap:24px;margin-top:16px}
.social span{width:24px;height:24px;border-radius:4px;background:#9a9a9a}
.copyright{left:0;top:4670px;width:1200px;height:77px;display:flex;align-items:center;justify-content:center;font-size:13.5px;color:#444}
</style>
</head>
<body>

<header class="abs site-header">
  <div class="abs header-email">
    <span class="mail-dot"><svg width="16" height="12" viewBox="0 0 16 12"><rect x="0" y="0" width="16" height="12" rx="1.5" fill="#fff"/><path d="M0 1 L8 7 L16 1" stroke="#333" stroke-width="1.6" fill="none"/></svg></span>
    info@rkharbourexcursions.com
  </div>
  <nav class="abs nav"><span class="current">Home</span><span>About Us</span><span>Contact Us</span></nav>
</header>
<div class="abs brand">RK Harbour<br>Excursions</div>

<section class="abs hero" role="img" aria-label="Marina with moored fishing boats over calm blue water">
  <h1>Discover Your Thrilling West<br>Coast Adventure</h1>
  <a class="btn" href="#book">Book Your Charter Today</a>
</section>

<!-- intro -->
<section class="abs feature" style="left:0;top:738px;width:1200px;height:573px">
  <div class="abs panel-lav" style="left:0;top:0;width:484px;height:573px"></div>
  <div class="abs photo" role="img" aria-label="Video: guide on the boat holding a large salmon" style="left:74px;top:74px;width:513px;height:425px;background:linear-gradient(160deg,#6f7f94,#3d4c5f 55%,#5b6a5a)">
    <svg class="play" width="80" height="80" viewBox="0 0 80 80"><circle cx="40" cy="40" r="36" fill="none" stroke="#fff" stroke-width="5"/><path d="M31 24 L57 40 L31 56 Z" fill="#fff"/></svg>
  </div>
  <div class="abs" style="left:615px;top:118px;width:520px">
    <h2>Experience the Ultimate West Coast Adventure</h2>
    <p style="margin-top:22px">Welcome aboard the 22-foot Harbourline charter boat, where RK Harbour Excursions and the legendary Ray Keller await to take you on an unforgettable journey through the untamed beauty of Campbell River, British Columbia. Brace yourself for an adrenaline-pumping fishing and wildlife tour like no other!</p>
  </div>
</section>

<!-- catch -->
<section class="abs feature dark" style="left:0;top:1311px;width:1200px;height:506px">
  <div class="abs" role="img" aria-label="Young angler on a boat giving a thumbs up while a guide works the line" style="left:560px;top:0;width:640px;height:506px;background:linear-gradient(90deg,var(--navy) 0%,#4b5d8f 30%,#6f8db0 65%,#4d6f86 100%)"></div>
  <div class="abs" style="left:74px;top:148px;width:590px">
    <h2>Reel in Your Dream Catch</h2>
    <p style="margin-top:14px">With Ray Keller's expert guidance, you'll have the chance to reel in monstrous salmon and feisty cod. Prepare for an angler's dream come true as you witness the sheer power and excitement of landing your prized catch.</p>
  </div>
</section>

<!-- ocean giants -->
<section class="abs feature" style="left:0;top:1817px;width:1200px;height:575px">
  <div class="abs panel-lav" style="left:717px;top:0;width:483px;height:575px"></div>
  <div class="abs photo" role="img" aria-label="Boat wake trailing behind the outboard on open water" style="left:614px;top:75px;width:512px;height:425px;background:linear-gradient(175deg,#7c9a77 0%,#4e6e86 30%,#9fb6c9 60%,#e6e8ea 100%)"></div>
  <div class="abs" style="left:74px;top:106px;width:520px">
    <h2>Wild Encounters with Ocean Giants</h2>
    <p style="margin-top:20px">Immerse yourself in the awe-inspiring world of marine life. Get up close and personal with majestic humpback whales as they breach just a splash away from the boat. Glide alongside graceful orcas as they glide effortlessly through the waves. This is a once-in-a-lifetime opportunity to witness the magic of these gentle ocean giants in their natural habitat.</p>
  </div>
</section>

<!-- wildlife -->
<section class="abs feature dark" style="left:0;top:2392px;width:1200px;height:505px">
  <div class="abs" role="img" aria-label="Two smiling anglers fishing from the shore with forest behind" style="left:560px;top:0;width:640px;height:505px;background:linear-gradient(90deg,var(--navy) 0%,#45407a 30%,#6d6a80 65%,#4b5a48 100%)"></div>
  <div class="abs" style="left:74px;top:124px;width:600px">
    <h2>Awe-Inspiring Wildlife Moments</h2>
    <p style="margin-top:14px">Venture into the heart of the wilderness, where coastal bears fish for salmon, showcasing their incredible hunting skills. Look up to the sky as bald eagles soar with breathtaking elegance overhead. These captivating wildlife moments are sure to leave you speechless.</p>
  </div>
</section>

<!-- two columns -->
<section class="abs feature" style="left:0;top:2897px;width:1200px;height:773px">
  <div class="abs photo" role="img" aria-label="Carved wooden resort sign at the marina dock" style="left:74px;top:67px;width:513px;height:313px;background:linear-gradient(160deg,#5e7b6a,#8a6a52 50%,#6b7f86)"></div>
  <div class="abs photo" role="img" aria-label="White charter boat moored at the marina" style="left:614px;top:67px;width:512px;height:313px;background:linear-gradient(180deg,#6f8b6b 0%,#a9b9c6 40%,#e9ecef 65%,#3f5a76 100%)"></div>
  <div class="abs" style="left:74px;top:410px;width:513px">
    <h2>Prawning Adventure and Delicious Rewards</h2>
    <p style="margin-top:22px">Experience the thrill of pulling up prawn traps, brimming with delectable, fresh prawns ready to be savored. Take home a delicious bounty and share the taste of the West Coast with your loved ones over a special dinner.</p>
  </div>
  <div class="abs" style="left:614px;top:410px;width:520px">
    <h2>Act Now – Limited Slots Available!</h2>
    <p style="margin-top:22px">Don't miss out on this epic adventure – time is running out! The demand for our charters is soaring, and spots are filling up fast. Contact Ray Keller at 250-739-4216 or email <a href="#">lou@rkharbourexcursions.com</a> to secure your spot and create legendary memories.</p>
  </div>
</section>

<!-- call of the wild -->
<section class="abs dark" role="img" aria-label="Angler's hands on a rod beside a misty lake at dusk" style="left:0;top:3670px;width:1200px;height:322px;background:linear-gradient(90deg,#3a3375 0%,#2f2a6c 45%,#3e3a78 100%)">
  <h2 style="position:absolute;left:0;width:1200px;top:94px;text-align:center;font-size:40px;color:#fff">Answer the Call of the Wild</h2>
  <p style="position:absolute;left:150px;width:900px;top:160px;text-align:center">The untamed wilderness of Campbell River beckons you. Answer the call of the wild and embark on a journey that will ignite your sense of adventure and wonder.</p>
</section>

<!-- booking -->
<section id="book" class="abs" style="left:0;top:3992px;width:1200px;height:408px">
  <h2 style="position:absolute;left:0;width:1200px;top:46px;text-align:center;font-size:41px">Book Your Thrilling Charter Today!</h2>
  <p style="position:absolute;left:110px;width:980px;top:136px;text-align:center">Your heart-pounding West Coast adventure is just a call away! Grab your phone and dial 250-739-4216 or email <a href="#">lou@rkharbourexcursions.com</a> to lock in your spot. Ray Keller and RK Harbour Excursions are ready to make your dreams of an exhilarating West Coast experience come true.</p>
  <a class="btn" href="#" style="position:absolute;left:420px;top:276px">Book Your Charter Today</a>
</section>

<footer class="abs site-footer">
  <div class="abs foot-brand">RK Harbour<br>Excursions</div>
  <div class="abs foot-col" style="left:344px;top:38px;width:320px">
    <h3>About Us</h3>
    <p>Your Campbell River fishing charter begins with a reliable 23 foot Harbourline Walk Around operated by a fully licenced guide. Your safety and comfort are our main priorities.</p>
  </div>
  <div class="abs foot-col" style="left:734px;top:38px;width:360px">
    <h3>Address</h3>
    <div class="addr-row"><svg width="18" height="16" viewBox="0 0 18 16"><path d="M2 1 V15" stroke="#f76b0a" stroke-width="2"/><path d="M3 2 H15 L12 6 L15 10 H3 Z" fill="#f76b0a"/></svg><span>PO Box 417<br>Campbell River BC, V9W2L3, CA</span></div>
    <div class="addr-row"><svg width="18" height="14" viewBox="0 0 18 14"><rect width="18" height="14" rx="1.5" fill="#f76b0a"/><path d="M0 1 L9 8 L18 1" stroke="#2b2b2b" stroke-width="1.5" fill="none"/></svg><span>info@rkharbourexcursions.com</span></div>
    <div class="social" aria-label="Social links"><span></span><span></span><span></span><span></span></div>
  </div>
</footer>
<div class="abs copyright">Copyright © 2023 CompanyName. | All Rights Reserved.</div>

</body>
</html>
```